Hello,

I need a logo design for a card game we are developing for our friends. Our idea is to create a drinking and party game for our friend group. The game actually is completely finished only thing missing is the design of the cards text and the logo on the back.

Back-card logo should state "Midnight Pebble Riddles" in a cool print, and it should be eye-catching. Literally, we just want to see cool ideas and see what we like.

The front of the cards should be designed in a way that text inside them can be modified in an example "Photoshop".

The front card will only include text. Text should read in the cards in two ways up and down so it will be easy to read from both sides of the table.

You can use the sample text: "The one time I designed a card..."

```html
<!DOCTYPE html>
<html lang="en">
<head>
<meta charset="utf-8">
<title>Midnight Pebble Riddles – Card Back and Face</title>
<link rel="stylesheet" href="https://fonts.googleapis.com/css2?family=Abril+Fatface&display=swap">
<style>
  :root {
    --page-bg: #ffffff;
    --gold: #c9962e;
    --gold-bright: #d6a23a;
    --night-core: #2b0c63;
    --night-edge: #0c0045;
    --frame-grey: #cccccc;
    --rule-grey: #8a8a8a;
    --face-white: #ffffff;
  }

  * { box-sizing: border-box; margin: 0; padding: 0; }

  html, body {
    width: 1200px;
    height: 805px;
    overflow: hidden;
    background: var(--page-bg);
  }

  .sheet {
    position: relative;
    width: 1200px;
    height: 805px;
    font-family: "Abril Fatface", "Bodoni Moda", Didot, serif;
  }

  /* ---------- Card back ---------- */
  .card-back {
    position: absolute;
    left: 51px;
    top: 37px;
    width: 507px;
    height: 708px;
    background: radial-gradient(ellipse 70% 60% at 50% 48%, var(--night-core) 0%, #1c0656 55%, var(--night-edge) 100%);
    display: flex;
    align-items: center;
    justify-content: center;
  }

  .brand-name {
    display: flex;
    flex-direction: column;
    align-items: center;
    gap: 56px;
    color: var(--gold-bright);
    font-weight: 400;
    font-size: 88px;
    line-height: 1;
    text-align: center;
  }

  .brand-name span { display: block; }

  /* ---------- Card face ---------- */
  .card-face {
    position: absolute;
    left: 627px;
    top: 37px;
    width: 505px;
    height: 709px;
    border: 9px solid var(--frame-grey);
    background: var(--face-white);
  }

  .face-half {
    position: absolute;
    left: 0;
    width: 100%;
    height: 50%;
  }

  .face-half--top { top: 0; }

  .face-half--bottom {
    bottom: 0;
    transform: rotate(180deg);
  }

  .prompt {
    position: absolute;
    left: 40px;
    top: 38px;
    width: 420px;
    color: var(--gold);
    font-size: 47px;
    line-height: 67px;
    text-align: center;
  }

  .prompt .line { display: block; white-space: nowrap; }

  .prompt .quote-open {
    font-size: 76px;
    vertical-align: 14px;
    line-height: 0;
    margin-right: 2px;
  }

  .prompt .quote-close {
    position: absolute;
    left: 262px;
    top: 118px;
    font-size: 76px;
    line-height: 1;
  }

  /* ---------- Page rule ---------- */
  .page-rule {
    position: absolute;
    left: 0;
    top: 786px;
    width: 1200px;
    height: 4px;
    background: var(--rule-grey);
  }
</style>
</head>
<body>
  <main class="sheet">
    <section class="card-back" aria-label="Card back">
      <h1 class="brand-name">
        <span>Midnight</span>
        <span>Pebble</span>
        <span>Riddles</span>
      </h1>
    </section>

    <section class="card-face" aria-label="Card face">
      <div class="face-half face-half--top">
        <p class="prompt">
          <span class="line"><span class="quote-open">“</span>The one time I</span>
          <span class="line">designed a</span>
          <span class="line">card...</span>
          <span class="quote-close">”</span>
        </p>
      </div>
      <div class="face-half face-half--bottom" aria-hidden="true">
        <p class="prompt">
          <span class="line"><span class="quote-open">“</span>The one time I</span>
          <span class="line">designed a</span>
          <span class="line">card...</span>
          <span class="quote-close">”</span>
        </p>
      </div>
    </section>

    <div class="page-rule"></div>
  </main>
</body>
</html>
```